Tailbrook Website Design

Need a website for a Dog Grooiming business. Please make it simular to these:

https://www.furvanto.com
https://haulnorix.com
https://meadowpetrin.com
https://www.drivelumo.com/search/

```html
<!DOCTYPE html>
<html lang="en">
<head>
<meta charset="utf-8">
<title>Tailbrook – Doorstep Dog Grooming</title>
<link href="https://fonts.googleapis.com/css2?family=Oswald:wght@400;500;600&family=Montserrat:wght@400;500;600;700&display=swap" rel="stylesheet">
<style>
:root{
  --blue:#0d4594;
  --blue-deep:#12397a;
  --navy:#173a6b;
  --green:#7dbb2a;
  --green-dark:#68a51c;
  --text:#6d6d6d;
  --light:#f4f4f4;
  --white:#fff;
}
*{margin:0;padding:0;box-sizing:border-box}
html,body{width:1200px;height:4451px;overflow:hidden}
body{position:relative;font-family:'Montserrat',sans-serif;color:var(--text);background:var(--white)}
.abs{position:absolute}
.oswald{font-family:'Oswald',sans-serif}
.btn{position:absolute;display:flex;align-items:center;justify-content:center;border-radius:24px;font-family:'Oswald',sans-serif;font-size:14px;letter-spacing:2px;color:var(--white);font-weight:500;gap:6px}
.btn.blue{background:var(--blue)}
.btn.green{background:var(--green)}
.btn.outline{border:3px solid var(--white)}
.ph{position:absolute}

/* header */
.logo{left:94px;top:16px;font-family:'Oswald',sans-serif;font-size:46px;font-weight:600;color:var(--blue);letter-spacing:.5px}
.call-icon{left:864px;top:18px;width:48px;height:48px;border-radius:50%;background:var(--blue);display:flex;align-items:center;justify-content:center}
.call-label{left:946px;top:16px;font-family:'Oswald',sans-serif;font-size:13px;letter-spacing:1.5px;color:var(--green)}
.call-number{left:924px;top:32px;font-family:'Oswald',sans-serif;font-size:25px;font-weight:600;color:var(--blue)}
.nav{left:0;top:100px;width:1200px;height:56px;background:var(--blue)}
.nav a{position:absolute;top:19px;font-family:'Oswald',sans-serif;font-size:15px;color:var(--white);text-decoration:none}
.nav .active::after{content:"";position:absolute;left:-2px;right:-2px;top:31px;height:4px;background:var(--green)}

/* hero */
.hero-photo{left:0;top:156px;width:1200px;height:611px;background:linear-gradient(90deg,#f3efec 0%,#e9e2dc 40%,#c9a98a 60%,#dcd4cc 80%,#cfd8e6 100%)}
.hero-title{left:86px;top:290px;font-family:'Oswald',sans-serif;font-size:55px;font-weight:600;line-height:60px;color:var(--blue)}
.hero-title span{color:var(--green)}
.hero-text{left:92px;top:430px;width:390px;font-size:14px;line-height:24px;color:#8a8a8a}
.quote-ear{top:78px;width:0;height:0;border-bottom:22px solid var(--green-dark)}
.quote-head{left:750px;top:78px;width:356px;height:78px;background:var(--green);color:var(--white);font-family:'Oswald',sans-serif;font-size:28px;display:flex;align-items:center;justify-content:center}
.quote-body{left:750px;top:156px;width:356px;height:397px;background:var(--blue)}
.field{position:absolute;left:39px;width:291px;height:36px;background:var(--white);font-size:11px;color:#555;padding:10px 20px}
.quote-btn{position:absolute;left:39px;top:324px;width:291px;height:38px;background:var(--green);color:var(--white);font-family:'Oswald',sans-serif;font-size:17px;display:flex;align-items:center;justify-content:center;letter-spacing:.5px}

/* section heading */
.sec-title{font-family:'Oswald',sans-serif;font-size:36px;color:var(--blue);font-weight:500;text-align:center;width:1200px;left:0}
.rule{height:4px;width:74px;background:var(--green)}

/* steps */
.step{position:absolute;width:300px;text-align:center}
.step-ring{position:absolute;left:44px;top:0;width:212px;height:212px;border-radius:50%;border:3px solid var(--green);padding:5px}
.step-ring .ph{position:relative;width:100%;height:100%;border-radius:50%}
.badge{position:absolute;left:50px;top:4px;width:44px;height:44px;border-radius:50%;background:var(--green);border:3px solid var(--white);color:var(--white);font-family:'Oswald',sans-serif;font-size:24px;display:flex;align-items:center;justify-content:center}
.badge.blue{background:var(--blue)}
.step h3{position:absolute;top:234px;width:300px;font-family:'Oswald',sans-serif;font-size:19px;font-weight:500;color:var(--blue)}
.step p{position:absolute;top:270px;left:20px;width:260px;font-size:12.5px;line-height:23px}

/* about */
.about{left:0;top:1353px;width:1200px;height:555px;background:var(--light)}
.h2{font-family:'Oswald',sans-serif;font-size:36px;color:var(--blue);font-weight:500}
.h2 span{color:var(--green)}
.body-text{font-size:14px;line-height:26px}

/* services */
.svc{position:absolute;width:240px;height:240px;border-radius:50%;background:var(--white);text-align:center}
.svc .icon{position:absolute;left:88px;top:56px;width:64px;height:64px;border-radius:50%;background:#e7eef8}
.svc p{position:absolute;top:136px;width:240px;font-size:14px;font-weight:700;line-height:22px;color:var(--blue)}

/* testimonials */
.card{position:absolute;width:294px;height:200px;background:#eef1f5;padding:34px 30px;font-size:11.5px;font-style:italic;line-height:19px;color:#777}
.card::after{content:"";position:absolute;left:44px;bottom:-14px;border-left:12px solid transparent;border-right:12px solid transparent;border-top:14px solid #eef1f5}
.reviewer{position:absolute;height:44px}
.avatar{position:absolute;left:0;top:0;width:44px;height:44px;border-radius:50%;background:linear-gradient(#d9b59a,#a06a4b)}
.rname{position:absolute;left:55px;top:4px;font-size:11px;font-weight:700;color:var(--blue);white-space:nowrap}
.stars{position:absolute;left:54px;top:17px;font-size:18px;color:#f59b12;letter-spacing:1px;white-space:nowrap}

/* footer */
.footer{left:0;top:4010px;width:1200px;height:441px;background:var(--navy)}
.fh{position:absolute;font-size:17px;color:var(--white);font-weight:500;letter-spacing:.5px}
.fl{position:absolute;font-size:13px;line-height:29px;color:#c8d3e6}
.social{position:absolute;width:26px;height:26px;border-radius:50%;background:var(--white)}
</style>
</head>
<body>

<!-- header -->
<div class="abs logo">Tailbrook</div>
<div class="abs call-icon">
  <svg width="24" height="24" viewBox="0 0 24 24"><path d="M6.6 10.8a15 15 0 0 0 6.6 6.6l2.2-2.2a1 1 0 0 1 1-.25 11.4 11.4 0 0 0 3.6.6 1 1 0 0 1 1 1V20a1 1 0 0 1-1 1A17 17 0 0 1 3 4a1 1 0 0 1 1-1h3.5a1 1 0 0 1 1 1c0 1.25.2 2.45.57 3.57a1 1 0 0 1-.25 1z" fill="none" stroke="#fff" stroke-width="1.6"/></svg>
</div>
<div class="abs call-label">REQUEST A CALL NOW</div>
<div class="abs call-number">1-800-555-0142</div>

<nav class="abs nav">
  <a class="active" style="left:108px">ABOUT US</a>
  <a style="left:216px">SERVICES</a>
  <a style="left:320px">TESTIMONIALS</a>
  <a style="left:436px">BLOGS</a>
  <a style="left:522px">FREE QUOTE</a>
  <a style="left:642px">CONTACT</a>
</nav>

<!-- hero -->
<div class="ph hero-photo" role="img" aria-label="Groomer blow-drying a small terrier on a grooming table"></div>
<div class="abs hero-title">DOORSTEP DOG<br><span>GROOMING</span></div>
<div class="abs hero-text">Lorem ipsum dolor sit amet, consectetur adipscing elit, sed do eiusmod tempor incididunt.</div>
<div class="btn green" style="left:86px;top:507px;width:179px;height:46px">BOOK ONLINE
  <svg width="18" height="10" viewBox="0 0 18 10"><path d="M0 5h16M12 1l4 4-4 4" stroke="#fff" stroke-width="1.5" fill="none"/></svg></div>

<div class="abs quote-ear" style="left:725px;border-left:25px solid transparent"></div>
<div class="abs quote-ear" style="left:1106px;border-right:25px solid transparent"></div>
<div class="abs quote-head">REQUEST A FREE QUOTES</div>
<form class="abs quote-body">
  <div class="field" style="top:40px">Your Name</div>
  <div class="field" style="top:90px">Email Address</div>
  <div class="field" style="top:139px">Phone Number</div>
  <div class="field" style="top:187px">Contact Prefer time</div>
  <div class="field" style="top:234px;height:73px">Your Message</div>
  <div class="quote-btn">GET QUOTE NOW</div>
</form>

<!-- how it works -->
<div class="abs sec-title" style="top:823px">HOW IT WORKS</div>
<div class="abs rule" style="left:563px;top:876px"></div>

<div class="step" style="left:145px;top:940px">
  <div class="step-ring"><div class="ph" style="background:linear-gradient(#0d4594 50%,#dfe6ee 50%)" role="img" aria-label="Laptop showing the booking page"></div></div>
  <div class="badge">1</div>
  <h3>SCHEDULE APPOINTMENT</h3>
  <p>Lorem ipsum dolor sit amet, consectetur adipiscing elit, sed do eiusm</p>
</div>
<div class="step" style="left:458px;top:940px">
  <div class="step-ring"><div class="ph" style="background:linear-gradient(135deg,#7dbb2a,#9ccd52)" role="img" aria-label="White grooming van"></div></div>
  <div class="badge blue">2</div>
  <h3>OUR EXPERT COME</h3>
  <p>Lorem ipsum dolor sit amet, consectetur adipiscing elit, sed do eiusm</p>
</div>
<div class="step" style="left:787px;top:940px">
  <div class="step-ring"><div class="ph" style="background:linear-gradient(90deg,#b86a44,#d8a37f)" role="img" aria-label="Poodle before and after grooming"></div></div>
  <div class="badge">3</div>
  <h3>GROOMING DONE!</h3>
  <p>Lorem ipsum dolor sit amet, consectetur adipiscing elit, sed do eiusm</p>
</div>

<!-- about -->
<div class="abs about"></div>
<svg class="abs" style="left:0;top:1353px" width="610" height="555" viewBox="0 0 610 555">
  <path d="M0 0H484C640 180 620 400 468 555H0Z" fill="#7dbb2a"/>
  <path d="M0 0H470C612 180 596 400 452 555H0Z" fill="#c9a27f" role="img" aria-label="Yorkshire terrier being combed by a groomer"/>
</svg>
<div class="abs h2" style="left:673px;top:1465px">ABOUT TAILBROOK</div>
<div class="abs rule" style="left:673px;top:1520px"></div>
<div class="abs body-text" style="left:673px;top:1545px;width:440px">Lorem ipsum dolor sit amet, consectetur adipiscing elit, sed do eiusmod tempor incididunt ut labore et dolor</div>
<div class="abs body-text" style="left:673px;top:1602px;width:440px">Ut enim ad minim veniam, quis nostrud exercitation ullamco laboris nisi ut aliquip ex ea commodo consequat. Duis aute irure dolor in reprehenderi.</div>
<div class="btn blue" style="left:670px;top:1709px;width:165px;height:42px">LEARN MORE</div>
<div class="btn green" style="left:840px;top:1709px;width:165px;height:42px">
  <svg width="12" height="12" viewBox="0 0 24 24"><path d="M6.6 10.8a15 15 0 0 0 6.6 6.6l2.2-2.2a1 1 0 0 1 1-.25 11.4 11.4 0 0 0 3.6.6 1 1 0 0 1 1 1V20a1 1 0 0 1-1 1A17 17 0 0 1 3 4a1 1 0 0 1 1-1h3.5a1 1 0 0 1 1 1c0 1.25.2 2.45.57 3.57a1 1 0 0 1-.25 1z" fill="#fff"/></svg>CALL US</div>

<!-- services -->
<svg class="abs" style="left:0;top:1908px" width="1200" height="544" viewBox="0 0 1200 544">
  <defs><linearGradient id="greenBg" x1="0" y1="0" x2="1" y2="1"><stop offset="0" stop-color="#86c232"/><stop offset="1" stop-color="#6aab1d"/></linearGradient></defs>
  <rect width="1200" height="544" fill="url(#greenBg)"/>
  <path d="M900 0H1200V544H640C660 300 740 80 900 0Z" fill="#1c4c9c" role="img" aria-label="Dog being groomed, tinted blue"/>
</svg>
<div class="abs oswald" style="left:128px;top:1978px;font-size:14px;color:#fff">WHAT WE DO</div>
<div class="abs oswald" style="left:128px;top:1995px;font-size:38px;color:#fff;font-weight:500">SERVICES PROVIDE</div>
<div class="abs" style="left:128px;top:2048px;width:320px;font-size:13.5px;line-height:23px;color:#fff">Lorem ipsum dolor sit amet, consectetur adipiscing elit sed do eiusmod</div>
<div class="svc" style="left:95px;top:2113px"><div class="icon" role="img" aria-label="Dog bath icon"></div><p>Bath with Shampoo<br>and Conditioner</p></div>
<div class="svc" style="left:352px;top:2113px"><div class="icon" role="img" aria-label="Clipper icon"></div><p>Full Body Trimming<br>and Styling</p></div>
<div class="svc" style="left:606px;top:2113px"><div class="icon" role="img" aria-label="Dog face icon"></div><p>Eyes &amp; Ears<br>Cleaning</p></div>
<div class="svc" style="left:862px;top:2113px"><div class="icon" role="img" aria-label="Breed grooming icon"></div><p style="top:142px">Breed Specific Pro<br>Grooming</p></div>

<!-- testimonials -->
<div class="abs oswald" style="left:0;width:1200px;text-align:center;top:2520px;font-size:14px;color:var(--blue)">OUR REVIEWS</div>
<div class="abs sec-title" style="top:2540px;font-size:34px">CUSTOMER <span style="color:var(--green)">TESTIMONIAL</span></div>

<div class="card" style="left:140px;top:2628px">Lorem ipsum dolor sit amet, consectetur adipiscing elit, sed do eiusmod tempor incididunt ut labore et dolore magna aliqua. Ut enim ad minim veniam, quis nostrud exercitation ullamco laboris nisi ut aliquip ex ea commodo conseq</div>
<div class="card" style="left:458px;top:2628px">Lorem ipsum dolor sit amet, consectetur adipiscing elit, sed do eiusmod tempor incididunt ut labore et dolore magna aliqua. Ut enim ad minim veniam, quis nostrud exercitation ullamco laboris nisi ut aliquip ex ea commodo conseq</div>
<div class="card" style="left:768px;top:2628px">Lorem ipsum dolor sit amet, consectetur adipiscing elit, sed do eiusmod tempor incididunt ut labore et dolore magna aliqua. Ut enim ad minim veniam, quis nostrud exercitation ullamco laboris nisi ut aliquip ex ea commodo conseq</div>

<div class="reviewer" style="left:174px;top:2848px"><div class="avatar" role="img" aria-label="Reviewer portrait"></div><div class="rname">Dana Merrow</div><div class="stars">★★★★★</div></div>
<div class="reviewer" style="left:493px;top:2848px"><div class="avatar" role="img" aria-label="Reviewer portrait"></div><div class="rname">Dana Merrow</div><div class="stars">★★★★★</div></div>
<div class="reviewer" style="left:802px;top:2848px"><div class="avatar" role="img" aria-label="Reviewer portrait"></div><div class="rname">Dana Merrow</div><div class="stars">★★★★★</div></div>

<!-- book -->
<div class="ph" style="left:0;top:2990px;width:1200px;height:550px;background:linear-gradient(90deg,#1a4aa0,#2457ad 50%,#1a4aa0)" role="img" aria-label="Small dog in grooming salon, tinted blue"></div>
<div class="abs oswald" style="left:110px;top:3095px;font-size:42px;line-height:50px;font-weight:500;color:#fff">BOOK YOUR<br><span style="color:var(--green)">DOG GROOMING</span></div>
<div class="abs" style="left:110px;top:3222px;width:390px;font-size:15px;line-height:26px;color:#fff">Lorem ipsum dolor sit amet, consectetur adipiscing elit, sed do eiusmod tempor incididunt ut labore et dolorUt enim ad minim\</div>
<div class="btn outline" style="left:115px;top:3332px;width:180px;height:44px">BOOK NOW</div>
<div class="btn green" style="left:300px;top:3332px;width:180px;height:44px">
  <svg width="12" height="12" viewBox="0 0 24 24"><path d="M6.6 10.8a15 15 0 0 0 6.6 6.6l2.2-2.2a1 1 0 0 1 1-.25 11.4 11.4 0 0 0 3.6.6 1 1 0 0 1 1 1V20a1 1 0 0 1-1 1A17 17 0 0 1 3 4a1 1 0 0 1 1-1h3.5a1 1 0 0 1 1 1c0 1.25.2 2.45.57 3.57a1 1 0 0 1-.25 1z" fill="#fff"/></svg>CALL US</div>
<svg class="abs" style="left:560px;top:3030px" width="510" height="490" viewBox="0 0 510 490">
  <path d="M255 480C110 430 10 330 20 210 30 110 110 60 190 80 230 40 280 10 360 10 450 20 500 90 495 190 490 320 400 430 255 480Z" fill="#fff" stroke="#7dbb2a" stroke-width="8"/>
  <path d="M255 462C122 414 32 322 40 212 48 124 118 82 192 102 232 62 282 32 358 32 436 42 478 102 474 190 470 310 388 414 255 462Z" fill="#c49a72" role="img" aria-label="Wet terrier being towel-dried"/>
</svg>

<!-- location -->
<div class="ph" style="left:110px;top:3632px;width:485px;height:305px;border-radius:40px 30px 60px 50px;background:linear-gradient(135deg,#1f5cc9,#6da6f0 50%,#bcd7fb)" role="img" aria-label="Map of the United States showing service areas"></div>
<div class="abs oswald" style="left:648px;top:3641px;font-size:14px;color:var(--blue)">AREA WE COVER</div>
<div class="abs h2" style="left:646px;top:3662px;font-size:33px">LOCATION WE <span>SERVE</span></div>
<div class="abs body-text" style="left:648px;top:3728px;width:370px;font-size:14.5px">Lorem ipsum dolor sit amet, consectetur adipiscing elit, sed do eiusmod tempor incididunt ut labore et dolorUt enim ad</div>
<div class="btn blue" style="left:654px;top:3830px;width:152px;height:38px;font-size:12px">LEARN MORE</div>

<!-- footer -->
<footer class="abs footer">
  <div class="fh" style="left:126px;top:100px">NAVIGATION</div>
  <div class="fl" style="left:129px;top:134px">Home<br>About Us<br>Grooming Services<br>Why We Are</div>
  <div class="fl" style="left:306px;top:134px">Testimonials<br>Book Online Now<br>Blogs<br>Contact Us</div>
  <div class="social" style="left:138px;top:282px"></div>
  <div class="social" style="left:172px;top:282px"></div>
  <div class="social" style="left:206px;top:282px"></div>

  <div class="fh" style="left:533px;top:102px">LOCATION WE SERVE</div>
  <div class="fl" style="left:534px;top:134px">Lorem ipsum dolor<br>Sit amet consectetur<br>Adipiscing elit<br>Eed do eiusmod<br>Tempor</div>

  <div class="fh" style="left:856px;top:100px">CONTACT US</div>
  <svg class="abs" style="left:852px;top:140px" width="34" height="34" viewBox="0 0 24 24"><path d="M6.6 10.8a15 15 0 0 0 6.6 6.6l2.2-2.2a1 1 0 0 1 1-.25 11.4 11.4 0 0 0 3.6.6 1 1 0 0 1 1 1V20a1 1 0 0 1-1 1A17 17 0 0 1 3 4a1 1 0 0 1 1-1h3.5a1 1 0 0 1 1 1c0 1.25.2 2.45.57 3.57a1 1 0 0 1-.25 1z" fill="none" stroke="#fff" stroke-width="1.3"/></svg>
  <div class="abs" style="left:898px;top:138px;font-size:13px;font-weight:700;color:#fff">PHONE NUMBER</div>
  <div class="abs" style="left:896px;top:160px;font-size:13px;color:#c8d3e6">(580) 555-0187</div>
  <svg class="abs" style="left:852px;top:210px" width="34" height="34" viewBox="0 0 34 34"><circle cx="17" cy="17" r="14" fill="none" stroke="#fff" stroke-width="2"/><path d="M10 17l5 5 10-11" fill="none" stroke="#fff" stroke-width="2.4"/></svg>
  <div class="abs" style="left:898px;top:210px;font-size:13px;font-weight:700;color:#fff">WORKING HOURS</div>
  <div class="abs" style="left:898px;top:232px;font-size:13px;line-height:25px;color:#c8d3e6">Mon- Fri: 7:00 Am to 9:00 Pm<br>Sat-Sun: 8:00 Am to 5:00 Pm</div>

  <div class="abs" style="left:0;top:362px;width:1200px;height:1px;background:#2d5087"></div>
  <div class="abs" style="left:0;top:388px;width:1200px;text-align:center;font-size:11px;color:#c8d3e6">© 2020 Tailbrook All Rights Reserved.</div>
</footer>

</body>
</html>
```